Paint Protection Options

This is a flyer that will describe two different paint protection options for vehicles. I have mocked up a Word doc. As well, I've included some samples of other flyers where I like the "look". I am not locked into any single layout or design. In my Word doc I have them side-by-side. I think that makes sense but open to ideas. I've also added some pics of the two options being applied to cars. We need to have one of each (ceramic and ppf) at a minimum. In the grid I'm thinking different colors dots/circles to differentiate the different levels. But again, I'm open to suggestions. You can use the symbol for microns in the grid under the Thickness row. I spelled it out because I didn't know how to insert.

```html
<!DOCTYPE html>
<html lang="en">
<head>
<meta charset="utf-8">
<title>Paint Protection Options – Flyer</title>
<link rel="stylesheet" href="https://fonts.googleapis.com/css2?family=Montserrat:wght@600;700;800;900&family=Open+Sans:wght@400;700&display=swap">
<style>
  :root{
    --backdrop:#8b8b8b;
    --paper:#ffffff;
    --brand-blue:#2c2f9c;
    --brand-red:#c8161d;
    --navy:#151a2a;
    --ppf-top:#4446c4;
    --ppf-bottom:#272a8c;
    --wax-blue:#1f9ae0;
    --ppf-col:#4b4fb0;
    --dot-green:#3aa55c;
    --dot-yellow:#f2b705;
    --dot-red:#d21f26;
    --ink:#1d1d25;
    --label-dark:#2a2e3a;
    --heading:'Montserrat', Arial, sans-serif;
    --body:'Open Sans', Arial, sans-serif;
  }
  *{box-sizing:border-box;margin:0;padding:0}
  html,body{width:1200px;height:882px;overflow:hidden}
  body{background:var(--backdrop);position:relative;font-family:var(--body);color:var(--ink)}

  .page{position:absolute;top:93px;width:544px;height:704px;background:var(--paper);overflow:hidden;box-shadow:0 2px 8px rgba(0,0,0,.25)}
  .page--front{left:45px}
  .page--back{left:612px}

  /* ---------- front header ---------- */
  .hero-band{position:absolute;left:0;top:164px;width:300px;height:25px;background:linear-gradient(90deg,#b9d4ea,#dbe8f3)}
  .hero-photo{position:absolute;left:0;top:0;width:544px;height:189px;
    background:linear-gradient(120deg,#dfe8f2 0%,#8fa3bb 30%,#1c2434 55%,#3a4a62 75%,#b9c8d8 100%);
    clip-path:polygon(301px 0,100% 0,100% 100%,235px 100%)}
  .hero-panel{position:absolute;left:0;top:0;width:544px;height:164px;background:var(--paper);
    clip-path:polygon(0 0,301px 0,243px 164px,0 164px)}
  .front-title{position:absolute;left:18px;top:18px;font-family:var(--heading);font-weight:900;line-height:1}
  .front-title__main{display:block;font-size:60px;color:var(--brand-blue);letter-spacing:-1px}
  .front-title__sub{display:block;font-size:29px;color:var(--brand-red);margin-top:4px}
  .front-title__outline{display:flex;align-items:center;gap:8px;font-size:26px;color:var(--paper);-webkit-text-stroke:1.4px var(--brand-blue);margin-top:3px}
  .front-title__rule{width:60px;height:2px;background:var(--brand-blue)}

  /* ---------- option cards ---------- */
  .option{position:absolute;top:240px;width:244px;height:306px;border-radius:10px}
  .option--ceramic{left:23px;background:linear-gradient(180deg,#b9bac4 0%,#eeeef2 45%,#d6d7de 100%)}
  .option--ppf{left:281px;background:linear-gradient(180deg,var(--ppf-top) 0%,var(--ppf-bottom) 100%)}
  .option__banner{position:absolute;top:-25px;height:49px;display:flex;align-items:center;justify-content:center;text-align:center;
    font-family:var(--heading);font-weight:800;font-size:15px;line-height:1.1;color:#fff}
  .option--ceramic .option__banner{left:17px;width:212px;background:linear-gradient(180deg,#d51d24,#a80f15);clip-path:polygon(0 0,100% 0,96% 100%,4% 100%)}
  .option--ppf .option__banner{left:16px;width:211px;background:var(--navy);clip-path:polygon(0 0,100% 0,96% 100%,4% 100%)}
  .option__body{position:absolute;left:16px;right:16px;top:40px;font-size:9.4px;line-height:11.7px;text-align:justify}
  .option__body p+p{margin-top:11.7px}
  .option--ppf .option__body{color:#fff}

  .benefits{position:absolute;top:483px;width:225px;height:152px;background:var(--navy);border-radius:6px;padding:9px 0 0 12px}
  .benefits--ceramic{left:32px}
  .benefits--ppf{left:292px}
  .benefits__list{list-style:none;color:#fff;font-size:9.6px;line-height:11.7px}
  .benefits__list li{display:flex;align-items:flex-start;gap:6px}
  .benefits__list svg{flex:none;width:11px;height:11px;margin-top:1px}
  .benefits__photo{position:absolute;left:7px;right:7px;bottom:6px;height:83px;border:1px solid #fff}
  .benefits--ceramic .benefits__photo{background:linear-gradient(110deg,#2b2f3a 0%,#c2410f 45%,#e8641a 70%,#8a2a10 100%)}
  .benefits--ppf .benefits__photo{background:linear-gradient(110deg,#2a3648 0%,#9fb0c0 40%,#d9e2ea 60%,#3b4556 100%)}

  /* ---------- footer ---------- */
  .footer{position:absolute;left:0;bottom:0;width:544px;height:41px;font-family:var(--heading);font-weight:700;font-size:16px;color:#fff;letter-spacing:.5px}
  .footer__contact{position:absolute;inset:0;background:var(--brand-blue);clip-path:polygon(0 0,258px 0,274px 100%,0 100%);padding:12px 0 0 26px}
  .footer__web{position:absolute;inset:0;background:var(--navy);clip-path:polygon(266px 0,100% 0,100% 100%,282px 100%);text-align:right;padding:11px 22px 0 0}

  /* ---------- back header ---------- */
  .back-title{position:absolute;left:18px;top:18px;font-family:var(--heading);font-weight:900;font-size:30px;line-height:1.05}
  .back-title__blue{color:var(--brand-blue)}
  .back-title__red{color:var(--brand-red)}
  .back-title__tag{position:absolute;left:346px;top:0;width:198px;height:69px;background:var(--navy);clip-path:polygon(18px 0,100% 0,100% 100%,0 100%);
    font-family:var(--heading);font-weight:900;font-size:30px;color:#fff;padding:17px 0 0 30px}

  .gallery{position:absolute;left:0;top:72px;width:544px;height:160px;filter:drop-shadow(0 3px 3px rgba(0,0,0,.35))}
  .gallery__frame{position:absolute;inset:0;background:#fff;clip-path:polygon(76px 0,100% 0,100% 155px,16px 155px)}
  .gallery__shot{position:absolute;inset:0}
  .gallery__shot--wax{clip-path:polygon(81px 4px,230px 4px,180px 151px,22px 151px);background:linear-gradient(130deg,#b0131c 0%,#e0242c 45%,#f2c14a 60%,#7b0c12 100%)}
  .gallery__shot--ceramic{clip-path:polygon(234px 4px,374px 4px,329px 151px,185px 151px);background:linear-gradient(130deg,#0d2a80 0%,#1e4fc2 50%,#f08a3a 70%,#0b1f5e 100%)}
  .gallery__shot--film{clip-path:polygon(378px 4px,544px 4px,544px 151px,333px 151px);background:linear-gradient(130deg,#c9d3dc 0%,#6f7f90 35%,#2c3440 60%,#aab6c2 100%)}

  /* ---------- comparison table ---------- */
  .compare{position:absolute;left:0;top:0;width:544px;height:704px}
  .compare__labels{position:absolute;left:21px;top:299px;width:159px;height:344px;background:var(--label-dark);border-radius:8px 0 0 8px;padding-top:15px}
  .compare__label{height:26.1px;display:flex;align-items:center;padding-left:13px;font-family:var(--heading);font-weight:600;font-size:9.6px;color:#fff}

  .plan{position:absolute;top:249px;width:112px;height:394px;background:#fff;border:1.5px solid var(--plan);border-radius:9px;overflow:hidden}
  .plan--wax{left:180px;--plan:var(--wax-blue)}
  .plan--ceramic{left:297px;--plan:var(--brand-red)}
  .plan--ppf{left:413px;--plan:var(--ppf-col)}
  .plan__head{height:49px;background:var(--plan);display:flex;align-items:center;justify-content:center;text-align:center;font-family:var(--heading);font-weight:800;font-size:11.5px;line-height:1.05;color:#fff}
  .plan__rows{list-style:none;padding:15px 5px 0}
  .plan__row{height:26.1px;display:flex;align-items:center;justify-content:center;gap:5px;border-bottom:1px solid color-mix(in srgb,var(--plan) 45%,#fff);font-family:var(--heading);font-weight:600;font-size:8.6px;color:#444}
  .plan__row:last-child{border-bottom:none}
  .plan__row svg{width:14px;height:14px}
  .plan__row .meter{width:auto;height:10px}
</style>
</head>
<body>

<svg width="0" height="0" style="position:absolute" aria-hidden="true">
  <defs>
    <symbol id="dot-full" viewBox="0 0 20 20"><circle cx="10" cy="10" r="9.5" fill="var(--dot-green)"/></symbol>
    <symbol id="dot-red" viewBox="0 0 20 20"><circle cx="10" cy="10" r="9.5" fill="var(--dot-red)"/></symbol>
    <symbol id="dot-half" viewBox="0 0 20 20"><path d="M10 .5A9.5 9.5 0 0 0 10 19.5Z" fill="var(--dot-yellow)"/></symbol>
    <symbol id="dot-slice" viewBox="0 0 20 20"><path d="M10 10L10 .5A9.5 9.5 0 0 1 18.2 5.2Z" transform="rotate(60 10 10)" fill="var(--dot-yellow)"/></symbol>
    <symbol id="dot-three" viewBox="0 0 20 20"><path d="M10 10L10 .5A9.5 9.5 0 1 1 .5 10Z" fill="var(--dot-green)"/></symbol>
    <symbol id="hourglass" viewBox="0 0 10 12"><path d="M0 0H10V1.5H9L5.8 6 9 10.5H10V12H0V10.5H1L4.2 6 1 1.5H0Z" fill="currentColor"/><path d="M2.6 1.5H7.4L5 5Z" fill="#fff" opacity=".55"/></symbol>
    <symbol id="tick-red" viewBox="0 0 12 12"><circle cx="6" cy="6" r="5.2" fill="none" stroke="var(--dot-red)" stroke-width="1.2"/><path d="M3 6.2 5.2 8.3 11 1.8" fill="none" stroke="var(--dot-red)" stroke-width="1.6"/></symbol>
    <symbol id="tick-blue" viewBox="0 0 12 12"><circle cx="6" cy="6" r="5.2" fill="none" stroke="#6e72e0" stroke-width="1.2"/><path d="M3 6.2 5.2 8.3 11 1.8" fill="none" stroke="#8c90ff" stroke-width="1.6"/></symbol>
  </defs>
</svg>

<!-- ================= FRONT ================= -->
<section class="page page--front">
  <div class="hero-band"></div>
  <div class="hero-photo" role="img" aria-label="Close-up of a glossy dark car headlight and front fender"></div>
  <div class="hero-panel"></div>

  <h1 class="front-title">
    <span class="front-title__main">PAINT</span>
    <span class="front-title__sub">PROTECTION</span>
    <span class="front-title__outline">OPTIONS<span class="front-title__rule"></span></span>
  </h1>

  <article class="option option--ceramic">
    <h2 class="option__banner">CERAMIC COATINGS</h2>
    <div class="option__body">
      <p>Ceramic coatings are <b>liquid polymer coatings that bond to a vehicle’s painted surface.</b> The coatings are formulated to retain the showroom finish by protecting against corrosion and contaminants like UV damage, oxidation, road salt and acid rain. Ceramic coatings give your car a deep, glossy finish that reflects light and makes your paint look more vibrant while greatly extending the paint’s lifespan.</p>
      <p>The chemical bonding process improves color depth &amp; leaves a smooth finish. <b>The hydrophobic (water repellent) properties repel water and dirt as well as protect against damaging pollutants.</b> This makes care and maintenance a breeze while retaining the show room finish. Never wax again!</p>
    </div>
  </article>

  <article class="option option--ppf">
    <h2 class="option__banner">PAINT PROTECTION<br>FILM (PPF)</h2>
    <div class="option__body">
      <p>Paint Protection Film (PPF) is a <b>transparent, thermoplastic urethane film that is applied directly to the car’s painted surfaces.</b> PPF excels at shielding your vehicle from rock chips, scratches, and other physical damage. It has self-healing properties that can repair minor scratches and swirl marks over time.</p>
      <p>Every piece of PPF is custom cut to fit each panel of your vehicle and provide maximum coverage. <b>The film protects your vehicle from scratches, rock chips, staining, corrosion, fading, chemicals, insects, and road debris.</b> It helps keep your paint looking new, saving you money and improving your resale value.</p>
    </div>
  </article>

  <div class="benefits benefits--ceramic">
    <ul class="benefits__list">
      <li><svg><use href="#tick-red"/></svg>Enhance and retain showroom finish</li>
      <li><svg><use href="#tick-red"/></svg>Protect against corrosion &amp; contaminants</li>
      <li><svg><use href="#tick-red"/></svg>Reduce care and maintenance</li>
    </ul>
    <div class="benefits__photo" role="img" aria-label="Technician applying ceramic coating to an orange car"></div>
  </div>

  <div class="benefits benefits--ppf">
    <ul class="benefits__list">
      <li><svg><use href="#tick-blue"/></svg>Protect against rock chips, scratches,<br>and physical damage</li>
      <li><svg><use href="#tick-blue"/></svg>Easily repair minor scratches &amp; swirl marks</li>
      <li><svg><use href="#tick-blue"/></svg>Protect against corrosion &amp; contamin</li>
    </ul>
    <div class="benefits__photo" role="img" aria-label="Installers laying clear protection film over a car hood"></div>
  </div>

  <footer class="footer">
    <div class="footer__contact">CONTACT US</div>
    <div class="footer__web">WEBSITE.COM</div>
  </footer>
</section>

<!-- ================= BACK ================= -->
<section class="page page--back">
  <h1 class="back-title"><span class="back-title__blue">PAINT</span> <span class="back-title__red">PROTECTION</span></h1>
  <div class="back-title__tag">OPTIONS</div>

  <div class="gallery">
    <div class="gallery__frame"></div>
    <div class="gallery__shot gallery__shot--wax" role="img" aria-label="Hand waxing a red car with a yellow applicator pad"></div>
    <div class="gallery__shot gallery__shot--ceramic" role="img" aria-label="Cloth buffing ceramic coating on a blue car"></div>
    <div class="gallery__shot gallery__shot--film" role="img" aria-label="Installers stretching protection film over a car"></div>
  </div>

  <div class="compare">
    <div class="compare__labels">
      <div class="compare__label">DURATION</div>
      <div class="compare__label">THICKNESS</div>
      <div class="compare__label">GLOSS ENHANCEMENT</div>
      <div class="compare__label">ACID RAIN DAMAGE</div>
      <div class="compare__label">CORROSION PREVENTION</div>
      <div class="compare__label">UV/OXIDATION PROTECTION</div>
      <div class="compare__label">HARD WATER DAMAGE</div>
      <div class="compare__label">INSECT SPLATTER DAMAGE</div>
      <div class="compare__label">CHIP PROTECTION</div>
      <div class="compare__label">SCRATCH PROTECTION</div>
      <div class="compare__label">SWIRL PROTECTION</div>
      <div class="compare__label">APPLICATION COMPLEXITY</div>
    </div>

    <div class="plan plan--wax">
      <div class="plan__head">CAR WAX</div>
      <ul class="plan__rows">
        <li class="plan__row"><svg class="meter" viewBox="0 0 10 12" style="color:var(--wax-blue)"><use href="#hourglass"/></svg>2 - 4 WEEKS</li>
        <li class="plan__row"><svg class="meter" viewBox="0 0 12 10"><rect x="0" y="4.5" width="12" height="1" fill="var(--wax-blue)"/></svg>.5 - 1.5 MICRONS</li>
        <li class="plan__row"><svg><use href="#dot-full"/></svg></li>
        <li class="plan__row"><svg><use href="#dot-half"/></svg></li>
        <li class="plan__row"><svg><use href="#dot-half"/></svg></li>
        <li class="plan__row"><svg><use href="#dot-half"/></svg></li>
        <li class="plan__row"><svg><use href="#dot-slice"/></svg></li>
        <li class="plan__row"><svg><use href="#dot-slice"/></svg></li>
        <li class="plan__row"><svg><use href="#dot-red"/></svg></li>
        <li class="plan__row"><svg><use href="#dot-red"/></svg></li>
        <li class="plan__row"><svg><use href="#dot-red"/></svg></li>
        <li class="plan__row">LOW</li>
      </ul>
    </div>

    <div class="plan plan--ceramic">
      <div class="plan__head">CERAMIC<br>COATINGS</div>
      <ul class="plan__rows">
        <li class="plan__row"><svg class="meter" viewBox="0 0 22 12" style="color:var(--brand-red)"><use href="#hourglass" width="10" height="12"/><use href="#hourglass" x="12" width="10" height="12"/></svg>3 - 10 YEARS</li>
        <li class="plan__row"><svg class="meter" viewBox="0 0 12 10"><rect x="0" y="3" width="12" height="4" fill="var(--brand-red)"/></svg>7 - 10 MICRONS</li>
        <li class="plan__row"><svg><use href="#dot-full"/></svg></li>
        <li class="plan__row"><svg><use href="#dot-full"/></svg></li>
        <li class="plan__row"><svg><use href="#dot-full"/></svg></li>
        <li class="plan__row"><svg><use href="#dot-full"/></svg></li>
        <li class="plan__row"><svg><use href="#dot-three"/></svg></li>
        <li class="plan__row"><svg><use href="#dot-three"/></svg></li>
        <li class="plan__row"><svg><use href="#dot-slice"/></svg></li>
        <li class="plan__row"><svg><use href="#dot-slice"/></svg></li>
        <li class="plan__row"><svg><use href="#dot-red"/></svg></li>
        <li class="plan__row">MEDIUM</li>
      </ul>
    </div>

    <div class="plan plan--ppf">
      <div class="plan__head">PAINT<br>PROTECTION<br>FILM (PPF)</div>
      <ul class="plan__rows">
        <li class="plan__row"><svg class="meter" viewBox="0 0 34 12" style="color:var(--ppf-col)"><use href="#hourglass" width="10" height="12"/><use href="#hourglass" x="12" width="10" height="12"/><use href="#hourglass" x="24" width="10" height="12"/></svg>7 - 10 YEARS</li>
        <li class="plan__row"><svg class="meter" viewBox="0 0 10 10"><rect width="10" height="10" fill="var(--ppf-col)"/></svg>200 - 250 MICRONS</li>
        <li class="plan__row"><svg><use href="#dot-full"/></svg></li>
        <li class="plan__row"><svg><use href="#dot-full"/></svg></li>
        <li class="plan__row"><svg><use href="#dot-full"/></svg></li>
        <li class="plan__row"><svg><use href="#dot-full"/></svg></li>
        <li class="plan__row"><svg><use href="#dot-full"/></svg></li>
        <li class="plan__row"><svg><use href="#dot-full"/></svg></li>
        <li class="plan__row"><svg><use href="#dot-full"/></svg></li>
        <li class="plan__row"><svg><use href="#dot-full"/></svg></li>
        <li class="plan__row"><svg><use href="#dot-full"/></svg></li>
        <li class="plan__row">HIGH</li>
      </ul>
    </div>
  </div>

  <footer class="footer">
    <div class="footer__contact">CONTACT US</div>
    <div class="footer__web">WEBSITE.COM</div>
  </footer>
</section>

</body>
</html>
```